Two Wine Labels, One Red One White

We are looking to create a brand image for our wines. There are two requirements by law that we need, however beyond that, the creativity comes from the designer. Required are:
On The Red Slate, Alcohol 14.1White Label Alcohol 12.5, The Size, 750ML
SO One label for the red wine with alcohol at 14.1 in a 750 ML Bottle, and one Label for white with alcohol at 12.5 in a 750 ML bottle.

Hi All:
I have some more clarity to assist in the design work.
The Brand Name of the wine is Valmaren for both the red and the white
The name should appear as Valmaren with the Brackets around phonetical as seen here
[vahl-mah-ren] Both the word and the phonetical spelling should appear.
and can be seen on wordplenk.com The Brand Name text can be black
Label should be very light grey, I am trying to capture a Stone grey or texture from stone, although, NOT Marble.
The Red Slate, The word "Red" should be in red
The White Slate, The word "White" should be in White, all the original remaining elements remain as originally posted.

I look forward to hearing from you for any additional questions.
Updates

Just added a logo Not really seeing what we are trying to achieve, maybe using the logo in the design may assist

Target Market(s)

Wine Aficionados

Requirements
Must have
• Details described in Project Description above, these are required by law. The Name of the Brand will be posted shortly. For the moment if you take the project, just place red on one label and white on the other.
Nice to have
• These two wines are from California (USA), so the Sierra Nevada Mountains could be an inspiration, to outline of California or coast line, a vineyard (of course), a vine...We are in silicon valley, so there is a map of silicon valley with the Bay and ocean, something from a map could work, or let your creativity flow and not use any of these concepts.
Should not have
• I do not not care for decorative fonts, however all else is open

```html
<!DOCTYPE html>
<html lang="en">
<head>
<meta charset="utf-8">
<title>Valmaren — The Red Slate &amp; The White Slate</title>
<link rel="stylesheet" href="https://fonts.googleapis.com/css2?family=Cinzel:wght@400;600;700&family=Arimo:wght@700&display=swap">
<style>
  :root {
    --page: #ffffff;
    --red: #b42330;
    --red-dark: #96202a;
    --red-light: #c9303c;
    --grey: #c2c2c2;
    --grey-dark: #a9a9a9;
    --grey-light: #d4d4d4;
    --band: #f3f1ef;
    --band-line: #dcd8d4;
    --name-grey: #8e8e8e;
    --glass: #140709;
    --glass-edge: #32141a;
    --wordmark: #e4e4e4;
  }
  * { margin: 0; padding: 0; box-sizing: border-box; }
  html, body { width: 1200px; height: 852px; overflow: hidden; background: var(--page); }
  .board { position: relative; width: 1200px; height: 852px; }

  /* ---------- Label ---------- */
  .label {
    position: absolute;
    width: 287px; height: 372px;
    overflow: hidden;
    font-family: "Cinzel", Georgia, serif;
    transform-origin: top left;
  }
  .label--red { background: var(--red); }
  .label--white { background: var(--grey); }
  .label__map { position: absolute; inset: 0; }
  .label--red .label__map { background: linear-gradient(115deg, var(--red-dark) 0%, var(--red-dark) 38%, var(--red) 52%, var(--red-light) 100%); }
  .label--white .label__map { background: linear-gradient(115deg, var(--grey-dark) 0%, var(--grey-dark) 38%, var(--grey) 52%, var(--grey-light) 100%); }

  .label__band {
    position: absolute; left: 0; right: 0; top: 88px; height: 66px;
    background: var(--band);
    border-top: 2px solid var(--band-line);
    border-bottom: 2px solid var(--band-line);
    text-align: center;
  }
  .label__band::before, .label__band::after {
    content: ""; position: absolute; left: 0; right: 0; height: 1px; background: var(--band-line);
  }
  .label__band::before { top: 5px; }
  .label__band::after { bottom: 5px; }
  .label__name {
    display: block; margin-top: 11px;
    font-size: 30px; font-weight: 700; letter-spacing: 3px; line-height: 1;
  }
  .label__phonetic {
    display: block; margin-top: 5px;
    font-size: 9px; font-weight: 600; letter-spacing: 1px; line-height: 1;
  }
  .label--red .label__name, .label--red .label__phonetic { color: var(--red); }
  .label--white .label__name, .label--white .label__phonetic { color: var(--name-grey); }

  .label__title {
    position: absolute; left: 22px; top: 168px;
    font-size: 46px; font-weight: 700; line-height: 46px;
    color: transparent;
    -webkit-text-stroke: 1.3px;
  }
  .label--red .label__title { -webkit-text-stroke-color: var(--red-light); }
  .label--white .label__title { -webkit-text-stroke-color: var(--grey-light); }

  .label__facts {
    position: absolute; left: 24px; right: 24px; top: 338px;
    display: flex; justify-content: space-between;
    font-family: "Arimo", Arial, sans-serif; font-weight: 700;
    font-size: 14px; color: #ffffff; font-variant: small-caps;
  }

  /* ---------- Bottles ---------- */
  .bottle { position: absolute; top: 33px; width: 217px; height: 780px; }
  .bottle__glass { position: absolute; inset: 0; }
  .bottle .label { top: 364px; left: 19px; transform: scale(0.62, 0.645); }

  /* ---------- Vertical wordmark ---------- */
  .wordmark { position: absolute; left: 1022px; top: 30px; width: 160px; height: 810px; }
  .wordmark__name, .wordmark__phonetic {
    position: absolute; white-space: nowrap;
    transform-origin: top left; transform: rotate(-90deg);
    font-family: "Cinzel", Georgia, serif; color: var(--wordmark);
  }
  .wordmark__name { left: 0; top: 810px; width: 810px; font-size: 112px; font-weight: 600; letter-spacing: 22px; line-height: 96px; text-align: center; }
  .wordmark__phonetic { left: 112px; top: 628px; width: 400px; font-size: 33px; font-weight: 600; letter-spacing: 3px; line-height: 40px; text-align: center; }
</style>
</head>
<body>
<main class="board">

  <section class="label label--red" style="left:30px; top:33px;">
    <div class="label__map" role="img" aria-label="Textured coastline map of the bay and ocean in red tones"></div>
    <div class="label__band"><span class="label__name">Valmaren</span><span class="label__phonetic">[vahl-mah-ren]</span></div>
    <h2 class="label__title">The<br>Red<br>Slate</h2>
    <p class="label__facts"><span>Alcohol 14.1%</span><span>750ML</span></p>
  </section>

  <section class="label label--white" style="left:30px; top:452px;">
    <div class="label__map" role="img" aria-label="Textured coastline map of the bay and ocean in stone grey tones"></div>
    <div class="label__band"><span class="label__name">Valmaren</span><span class="label__phonetic">[vahl-mah-ren]</span></div>
    <h2 class="label__title">The<br>White<br>Slate</h2>
    <p class="label__facts"><span>Alcohol 12.5%</span><span>750ML</span></p>
  </section>

  <div class="bottle" style="left:418px;">
    <svg class="bottle__glass" role="img" aria-label="Dark wine bottle" viewBox="0 0 217 780" width="217" height="780">
      <defs><linearGradient id="glass" x1="0" x2="1"><stop offset="0" stop-color="var(--glass)"/><stop offset=".3" stop-color="var(--glass-edge)"/><stop offset="1" stop-color="var(--glass)"/></linearGradient></defs>
      <path d="M79 2h58v160c0 60 80 75 80 170v435c0 6-4 10-10 10H10c-6 0-10-4-10-10V332c0-95 79-110 79-170z" fill="url(#glass)"/>
    </svg>
    <section class="label label--red">
      <div class="label__map" role="img" aria-label="Textured coastline map in red tones"></div>
      <div class="label__band"><span class="label__name">Valmaren</span><span class="label__phonetic">[vahl-mah-ren]</span></div>
      <h2 class="label__title">The<br>Red<br>Slate</h2>
      <p class="label__facts"><span>Alcohol 14.1%</span><span>750ML</span></p>
    </section>
  </div>

  <div class="bottle" style="left:722px;">
    <svg class="bottle__glass" role="img" aria-label="Dark wine bottle" viewBox="0 0 217 780" width="217" height="780">
      <path d="M79 2h58v160c0 60 80 75 80 170v435c0 6-4 10-10 10H10c-6 0-10-4-10-10V332c0-95 79-110 79-170z" fill="url(#glass)"/>
    </svg>
    <section class="label label--white">
      <div class="label__map" role="img" aria-label="Textured coastline map in stone grey tones"></div>
      <div class="label__band"><span class="label__name">Valmaren</span><span class="label__phonetic">[vahl-mah-ren]</span></div>
      <h2 class="label__title">The<br>White<br>Slate</h2>
      <p class="label__facts"><span>Alcohol 12.5%</span><span>750ML</span></p>
    </section>
  </div>

  <div class="wordmark" aria-label="Valmaren [vahl-mah-ren]">
    <span class="wordmark__name">VALMAREN</span>
    <span class="wordmark__phonetic">[VAHL-MAH-REN]</span>
  </div>

</main>
</body>
</html>
```